Letterhead Design Project

Initially, we would like to review our letterheads.

Something simple which uses our corporate imagery well and is nicely balanced.

Please note that I will be following up this letter-head with some customised quote templates and similarly customisable collateral in the next few weeks.

Target Market(s)

Enterprise business

Industry/Entity Type

Quote

Requirements
Must have
• The Nexora9 logo
See www.nexora9.com.au

Our tagline "Enterprise Hosting, Messaging and Server Virtualisation"

Our website address

Ideally in our colour pallette, but will consider submissions which look fantastic and necessitate other colours.

```html
<!DOCTYPE html>
<html lang="en">
<head>
<meta charset="utf-8">
<title>Nexora9 Letterhead</title>
<link rel="stylesheet" href="https://fonts.googleapis.com/css2?family=Source+Sans+3:wght@400;600;700&family=Cinzel:wght@600&display=swap">
<style>
  :root {
    --brand-red: #c1272d;
    --ink: #1d1d1d;
    --text-grey: #555555;
    --rule-grey: #9a9a9a;
    --tint: #f9e5e5;
    --paper: #ffffff;
    --backdrop: #ffffff;
  }
  * { margin: 0; padding: 0; box-sizing: border-box; }
  html, body {
    width: 982px; height: 1200px; overflow: hidden;
    background: var(--backdrop);
  }
  .letterhead {
    position: relative;
    width: 982px; height: 1200px;
    background: var(--paper);
    font-family: "Source Sans 3", Arial, sans-serif;
    color: var(--text-grey);
  }
  .brand {
    position: absolute; left: 58px; top: 52px;
    display: flex; align-items: center; gap: 16px;
  }
  .brand-square {
    width: 58px; height: 58px; background: var(--brand-red);
  }
  .brand-name {
    font-weight: 700; font-size: 62px; line-height: 1;
    color: var(--ink); letter-spacing: -1px;
  }
  .contact {
    position: absolute; left: 743px; top: 58px;
    border-left: 1px solid var(--rule-grey);
    padding-left: 12px;
    font-size: 15px; line-height: 21px;
  }
  .contact-row { display: flex; align-items: center; gap: 5px; }
  .contact-row svg { width: 12px; height: 12px; fill: var(--text-grey); }
  .header-rule {
    position: absolute; top: 166px; height: 2px; background: var(--brand-red);
  }
  .header-rule.left { left: 0; width: 640px; }
  .header-rule.right { left: 886px; width: 96px; }
  .website {
    position: absolute; left: 663px; top: 156px;
    font-size: 15px; font-weight: 700; letter-spacing: 4px;
    color: var(--text-grey); line-height: 20px;
  }
  .brand-tint {
    position: absolute; left: 278px; top: 396px;
    width: 425px; height: 407px; background: var(--tint);
  }
  .company-address {
    position: absolute; left: 0; right: 0; top: 1130px;
    text-align: center; font-size: 14px; color: var(--text-grey);
  }
  .company-address strong { color: #3a3a3a; font-weight: 700; margin-right: 4px; }
  .tagline {
    position: absolute; left: 0; right: 0; top: 1160px;
    text-align: center; font-family: "Cinzel", Georgia, serif;
    font-weight: 600; font-size: 21px; letter-spacing: 1.5px;
    color: var(--brand-red);
  }
</style>
</head>
<body>
<main class="letterhead">
  <header>
    <div class="brand">
      <span class="brand-square"></span>
      <span class="brand-name">Nexora9</span>
    </div>
    <address class="contact" style="font-style:normal">
      <div class="contact-row">
        <svg viewBox="0 0 24 24" aria-hidden="true"><path d="M6.6 10.8a15 15 0 0 0 6.6 6.6l2.2-2.2a1 1 0 0 1 1-.25 11.4 11.4 0 0 0 3.6.6 1 1 0 0 1 1 1V20a1 1 0 0 1-1 1A17 17 0 0 1 3 4a1 1 0 0 1 1-1h3.5a1 1 0 0 1 1 1c0 1.25.2 2.45.6 3.6a1 1 0 0 1-.25 1z"/></svg>
        <span>+61 3 9000 4172</span>
      </div>
      <div class="contact-row">
        <svg viewBox="0 0 24 24" aria-hidden="true"><path d="M2 5h20v14H2z M3 6l9 7 9-7" /></svg>
        <span>info@nexora9.com.au</span>
      </div>
    </address>
    <div class="header-rule left"></div>
    <div class="website">www.nexora9.com.au</div>
    <div class="header-rule right"></div>
  </header>

  <div class="brand-tint"></div>

  <footer>
    <p class="company-address"><strong>Nexora9 Pty. Ltd.</strong> Suite 4, Level 3, 18 Harlow Parade, Elmsbury, Australia, VIC - 3999</p>
    <p class="tagline">Enterprise Hosting, Messaging and Server Virtualization</p>
  </footer>
</main>
</body>
</html>
```